Zielgruppe
Wir sind ein Fliesenlegerbetrieb und sind auf der suche nach Mitarbeitern / Fliesenleger. Unsere Kunden sind Privatkunden sowie Öffentliche und Gewerbliche Auftraggeber. Das design soll für Arbeitsuchende ansprechend sein und zu unserem CI passen. Inspiration zu unserem CI finden SIe unter www.fliesen-worlak.de
Aufgabenstellung
Es handelt sich um eine Stellenanzeige die wir im Format 90x50 mm quer und im Format 90 x 90 mm benötigen. In Farbe und S/W.
Unser Textvorschlag, Der Designer darf aucg selbst kreativ sein / werden.
Du arbeitest selbständig und verantwortungsbewusst, hast Freude am Kundenkontakt und kannst jedes Problem lösen ? Dann komm direkt zu uns !
Das erwartet Dich bei uns:
- Junges eingespieltes Team
- Sehr gutes Betriebsklima
- Faire Bezahlung
- Baustellenfahrzeug + Werkzeug
- Unbefristetes Arbeitsverhältnis
- Heimatnahe Baustellen
- Öffentliche, Gewerbliche, Private Baustellen
Kontaktdaden damit sich der Bewerber auch bei uns melden kann !

```html
<!DOCTYPE html>
<html lang="de">
<head>
<meta charset="utf-8">
<title>Stellenanzeige Fliesenleger</title>
<link href="https://fonts.googleapis.com/css2?family=Roboto:ital,wght@0,300;0,400;0,700;0,900;1,700&display=swap" rel="stylesheet">
<style>
  :root{
    --red:#d42027;
    --grey:#8f8f8f;
    --ink:#2b2b2b;
    --white:#ffffff;
  }
  *{margin:0;padding:0;box-sizing:border-box}
  html,body{width:1200px;height:1200px;overflow:hidden;background:var(--white);font-family:'Roboto',sans-serif}
  .ad{position:absolute;left:100px;top:325px;width:1007px;height:557px;background:var(--white);overflow:hidden}
  .ad__topbar{position:absolute;left:0;top:0;width:100%;height:11px;background:var(--grey)}
  .ad__lower{position:absolute;left:0;top:295px;width:100%;height:262px;background:var(--grey)}
  .ad__photo-frame{position:absolute;left:662px;top:51px;width:300px;height:506px;background:var(--grey)}
  .ad__photo{position:absolute;left:680px;top:69px;width:264px;height:419px;border-radius:9px;
    background:linear-gradient(150deg,#efe4d8 0%,#e6d8c9 45%,#c98c55 75%,#b94a3a 100%)}
  .brand{position:absolute;left:49px;top:60px;font-size:22px;font-weight:700;color:var(--ink);letter-spacing:.2px}
  .headline{position:absolute;left:49px;top:104px;color:var(--red);font-weight:900;font-size:29px;line-height:37px;letter-spacing:1.6px}
  .intro{position:absolute;left:49px;top:185px;width:560px;font-size:18px;line-height:27px;color:var(--ink);font-weight:400}
  .intro em{color:var(--red);font-weight:700;font-style:italic}
  .cta{position:absolute;left:49px;top:249px;font-size:22px;font-weight:300;color:var(--red)}
  .benefit{position:absolute;width:120px;text-align:center;color:#f4f4f4;font-size:9.5px;line-height:13px;letter-spacing:.6px}
  .benefit svg{display:block;margin:0 auto 6px}
  .contact{position:absolute;left:369px;top:432px;width:276px;height:80px;background:var(--red);
    border-radius:4px 12px 12px 12px;color:var(--white);font-size:14px;line-height:20.5px;padding:9px 0 0 38px}
  .post{position:absolute;top:512px;width:15px;height:45px;background:var(--white)}
</style>
</head>
<body>
<div class="ad">
  <div class="ad__topbar"></div>
  <div class="ad__lower"></div>
  <div class="ad__photo-frame"></div>
  <div class="ad__photo" role="img" aria-label="Foto: Hände eines Fliesenlegers setzen eine Fliese an eine Wand"></div>

  <div class="brand">Fliesen-Worlak</div>
  <h1 class="headline">STELLEN FÜR<br>FLIESENLEGER VERFÜGBAR.</h1>
  <p class="intro">Du arbeitest <em>selbständig</em> und <em>verantwortungsbewusst</em>, hast Freude am Kundenkontakt und kannst jedes <em>Problem lösen</em>?</p>
  <p class="cta">Dann komm direkt zu uns !</p>

  <div class="benefit" style="left:33px;top:317px">
    <svg width="45" height="45" viewBox="0 0 45 45"><circle cx="22.5" cy="22.5" r="22.5" fill="var(--red)"/><g fill="none" stroke="#fff" stroke-width="2.4"><circle cx="22.5" cy="15" r="4"/><circle cx="16" cy="26" r="4"/><circle cx="29" cy="26" r="4"/></g></svg>
    Junges<br>eingespieltes Team</div>
  <div class="benefit" style="left:147px;top:317px">
    <svg width="45" height="45" viewBox="0 0 45 45"><circle cx="22.5" cy="22.5" r="22.5" fill="var(--red)"/><rect x="13" y="16" width="19" height="14" rx="2" fill="#fff"/><rect x="18.5" y="12.5" width="8" height="4" rx="1" fill="none" stroke="#fff" stroke-width="2"/><line x1="13" y1="22" x2="32" y2="22" stroke="var(--red)" stroke-width="1.5"/></svg>
    Sehr<br>gutes Betriebsklima</div>
  <div class="benefit" style="left:261px;top:317px">
    <svg width="45" height="45" viewBox="0 0 45 45"><circle cx="22.5" cy="22.5" r="22.5" fill="var(--red)"/><text x="27" y="21" fill="#fff" font-size="13" font-weight="700" text-anchor="middle" font-family="Roboto,sans-serif">$</text><path d="M11 26h7l6 3h6l-2 3h-8m-9-1l9 3 12-4" fill="none" stroke="#fff" stroke-width="2" stroke-linejoin="round"/></svg>
    Faire<br>Bezahlung</div>
  <div class="benefit" style="left:375px;top:317px">
    <svg width="45" height="45" viewBox="0 0 45 45"><circle cx="22.5" cy="22.5" r="22.5" fill="var(--red)"/><path d="M14 17v10h17a3 3 0 0 0 0-6H18" fill="none" stroke="#fff" stroke-width="2.2"/><path d="M17 13v6M14 16h6" stroke="#fff" stroke-width="2"/></svg>
    Baustellenfahrzeug<br>+ Werkzeug</div>
  <div class="benefit" style="left:489px;top:317px">
    <svg width="45" height="45" viewBox="0 0 45 45"><circle cx="22.5" cy="22.5" r="22.5" fill="var(--red)"/><rect x="10" y="19" width="20" height="10" rx="1" fill="#e9f5ee"/><circle cx="20" cy="24" r="2.5" fill="#7bbf95"/><rect x="29" y="16" width="6" height="9" rx="1" fill="#f3d36b"/></svg>
    Unbefristetes<br>Arbeitsverhältnis</div>
  <div class="benefit" style="left:33px;top:422px">
    <svg width="45" height="45" viewBox="0 0 45 45"><circle cx="22.5" cy="22.5" r="22.5" fill="var(--red)"/><path d="M21 14v16M13 22h16" stroke="#fff" stroke-width="4"/><path d="M30 10v6M27 13h6" stroke="#fff" stroke-width="1.6"/></svg>
    Heimatnahe<br>Baustellen</div>
  <div class="benefit" style="left:147px;top:422px">
    <svg width="45" height="45" viewBox="0 0 45 45"><circle cx="22.5" cy="22.5" r="22.5" fill="var(--red)"/><g fill="#fff"><rect x="19.5" y="12" width="6" height="5"/><rect x="12" y="27" width="6" height="5"/><rect x="19.5" y="27" width="6" height="5"/><rect x="27" y="27" width="6" height="5"/></g><path d="M22.5 17v10M15 27v-4h15v4" fill="none" stroke="#fff" stroke-width="1.6"/></svg>
    Öffentliche, Gewerbliche,<br>Private Baustellen</div>

  <div class="contact">
    Telephone:&nbsp; 0 91 99 / 5 42 07 13<br>
    Mobile: 01 62 / 3 27 48 95<br>
    Email: info@fliesen-worlak.de
  </div>
  <div class="post" style="left:422px"></div>
  <div class="post" style="left:585px"></div>
</div>
</body>
</html>
```